Software Development Consulting Company Needs Business Card Design

We need a new business card design for our consultants at Verdant Systems (verdantsystems.example). We are a small firm that provides high-end software development and methodology consulting to medium to large enterprise IT organizations.

Our logo uses Futura for the font and we would like to stick with navy blue and canary yellow for the logo colors. Attached are normal and reversed versions of our logos in illustrator format.
Updates

Hi Everyone, Thank yo very much for your amazing design ideas. I have created a poll for this project and our employees will be voting on the design they wish to use. We will be making a decision this Wednesday (October 22nd). Thanks again, Marcus Hallward

Industry/Entity Type

Business

```html
<!DOCTYPE html>
<html lang="en">
<head>
<meta charset="utf-8">
<title>Verdant Systems – Business Card</title>
<link href="https://fonts.googleapis.com/css2?family=Jost:wght@400;500&display=swap" rel="stylesheet">
<style>
  :root {
    --navy: #1d3d63;
    --navy-deep: #132c4a;
    --canary: #d9cf1e;
    --paper: #f7f7f7;
    --paper-shade: #e6e6e6;
    --ink: #1d3d63;
    --stage: #2b2b2b;
  }
  * { box-sizing: border-box; margin: 0; padding: 0; }
  html, body { width: 1200px; height: 900px; overflow: hidden; }
  body {
    background: var(--stage);
    font-family: "Jost", "Futura", sans-serif;
    position: relative;
  }
  .card {
    position: absolute;
    left: 270px;
    width: 660px;
    height: 377px;
    border-radius: 28px;
    overflow: hidden;
    box-shadow: 0 10px 30px rgba(0,0,0,0.5);
  }
  /* Back side */
  .card-back {
    top: 48px;
    background: linear-gradient(160deg, var(--navy) 0%, var(--navy-deep) 100%);
    display: flex;
    align-items: center;
    justify-content: center;
  }
  .back-brand {
    display: flex;
    align-items: center;
    gap: 18px;
  }
  .back-brand .brand-name {
    color: #ffffff;
    font-size: 44px;
    font-weight: 500;
    letter-spacing: 0.08em;
  }
  .brand-dot {
    width: 22px;
    height: 22px;
    border-radius: 50%;
    background: var(--canary);
    flex: none;
  }
  /* Front side */
  .card-front {
    top: 475px;
    background: linear-gradient(150deg, var(--paper) 0%, #ffffff 45%, var(--paper-shade) 100%);
  }
  .front-brand {
    position: absolute;
    left: 44px;
    top: 38px;
    display: flex;
    align-items: center;
    gap: 14px;
  }
  .front-brand .brand-name {
    color: var(--ink);
    font-size: 40px;
    font-weight: 500;
    letter-spacing: 0.08em;
  }
  .website {
    position: absolute;
    left: 84px;
    top: 96px;
    color: var(--ink);
    font-size: 17px;
  }
  .person {
    position: absolute;
    left: 84px;
    top: 128px;
    color: var(--ink);
  }
  .person-name { font-size: 27px; font-weight: 400; line-height: 1.2; }
  .person-title { font-size: 17px; margin-top: 2px; }
  .contacts {
    position: absolute;
    left: 84px;
    top: 202px;
    list-style: none;
    color: var(--ink);
    font-size: 18px;
  }
  .contacts li {
    display: flex;
    align-items: center;
    gap: 10px;
    height: 28px;
  }
  .contacts svg { width: 16px; height: 16px; flex: none; }
  .address-band {
    position: absolute;
    left: 0;
    right: 0;
    bottom: 0;
    height: 52px;
    background: var(--navy);
    color: var(--canary);
    font-size: 19px;
    display: flex;
    align-items: center;
    padding-left: 84px;
    letter-spacing: 0.02em;
  }
</style>
</head>
<body>
  <section class="card card-back" aria-label="Card back">
    <div class="back-brand">
      <span class="brand-dot"></span>
      <span class="brand-name">Verdant Systems</span>
    </div>
  </section>

  <section class="card card-front" aria-label="Card front">
    <div class="front-brand">
      <span class="brand-dot"></span>
      <span class="brand-name">Verdant Systems</span>
    </div>
    <p class="website">www.verdantsystems.example</p>
    <div class="person">
      <p class="person-name">Marcus Hallward</p>
      <p class="person-title">Principal Consultant</p>
    </div>
    <ul class="contacts">
      <li>
        <svg viewBox="0 0 16 16" aria-hidden="true"><rect x="4" y="1" width="8" height="14" rx="1.5" fill="none" stroke="#1d3d63" stroke-width="1.6"/><circle cx="8" cy="12.3" r="0.9" fill="#1d3d63"/></svg>
        555-014-2290
      </li>
      <li>
        <svg viewBox="0 0 16 16" aria-hidden="true"><rect x="1" y="3.5" width="14" height="9" fill="#1d3d63"/><path d="M1 3.5 L8 9 L15 3.5" fill="none" stroke="#f7f7f7" stroke-width="1.2"/></svg>
        marcus.hallward@verdantsystems.example
      </li>
      <li>
        <svg viewBox="0 0 16 16" aria-hidden="true"><rect x="1.5" y="1.5" width="13" height="13" rx="2" fill="#1d3d63"/></svg>
        @mhallward
      </li>
    </ul>
    <div class="address-band">4410 Harbor Point Dr, Riverton, OH 45012</div>
  </section>
</body>
</html>
```